Business Card Design

Very plain simple card, Plain modern font. Background. Grey fading to black. Large Bright lime green text. Saying.

TWR-ZA.COM

Small other details in white text.

Irish Horse Sales . Livery . Stud . Shows

Mark Dabrowski
TWR
Birch Lodge
Carrowmede Lane
Thistlecombe
Lincolnshire
LN4 7JX

Email. Twrzap@mailvale.co.uk
Tel. 07482 936504

Industry/Entity Type

Business

Contact Information for Business Card

As below

```html
<!DOCTYPE html>
<html lang="en">
<head>
<meta charset="utf-8">
<title>TWR-ZA.COM Business Card</title>
<link href="https://fonts.googleapis.com/css2?family=Jura:wght@400;500&display=swap" rel="stylesheet">
<style>
  :root {
    --page-bg: #f2f2f4;
    --card-grey: #6d6d71;
    --lime: #c8dc28;
    --white: #ffffff;
  }
  html, body {
    margin: 0;
    padding: 0;
    width: 1200px;
    height: 1000px;
    overflow: hidden;
    background: var(--page-bg);
  }
  .card {
    position: absolute;
    left: 365px;
    top: 347px;
    width: 512px;
    height: 290px;
    background: var(--card-grey);
    font-family: "Jura", sans-serif;
  }
  .name-band {
    position: absolute;
    left: 0;
    top: 99px;
    width: 100%;
    height: 92px;
    background: var(--lime);
  }
  .brand-name {
    position: absolute;
    left: 86px;
    top: 10px;
    margin: 0;
    font-size: 64px;
    font-weight: 400;
    letter-spacing: 1px;
    color: var(--card-grey);
    line-height: 1.2;
    white-space: nowrap;
  }
  .services {
    position: absolute;
    top: 213px;
    left: 0;
    width: 100%;
    margin: 0;
    text-align: center;
    font-size: 15px;
    color: var(--white);
    letter-spacing: 0.2px;
  }
  .services .dot-accent { color: var(--lime); }
  .contact {
    position: absolute;
    top: 248px;
    display: flex;
    align-items: center;
    font-size: 15px;
    color: var(--white);
    white-space: nowrap;
  }
  .contact-email { left: 47px; }
  .contact-phone { left: 311px; }
  .contact-marker {
    width: 14px;
    height: 25px;
    margin-right: 3px;
  }
</style>
</head>
<body>
  <div class="card">
    <div class="name-band">
      <h1 class="brand-name">TWR-ZA.COM</h1>
    </div>
    <p class="services">Irish Horse Sales <span class="dot-accent">.</span> Livery . Stud <span class="dot-accent">.</span> Shows</p>
    <div class="contact contact-email">
      <svg class="contact-marker" viewBox="0 0 14 25" aria-hidden="true">
        <rect x="0" y="0" width="3" height="25" fill="var(--lime)"/>
        <rect x="9" y="0" width="3" height="25" fill="var(--lime)"/>
      </svg>
      <span>Email. Twrzap@mailvale.co.uk</span>
    </div>
    <div class="contact contact-phone">
      <svg class="contact-marker" viewBox="0 0 14 25" aria-hidden="true">
        <rect x="0" y="0" width="3" height="25" fill="var(--lime)"/>
        <rect x="9" y="0" width="3" height="25" fill="var(--lime)"/>
      </svg>
      <span>Tel. 07482 936504</span>
    </div>
  </div>
</body>
</html>
```